New Business Cards for Velmora

About Velmora:
At Velmora, we're more than just a company—we're a force for positive change in the staffing industry. Our brand is our heartbeat, and we need a designer who can translate that into every design element.

The Project:
We're revamping our business cards and need your artistic flair to make them stand out. Here's what we're looking for:

- Incorporate our existing brand elements (logo, colours, fonts) into the design.
- Craft a design that's sleek, professional, and memorable.
- Provide options for different layouts and finishes.
- Collaborate closely with our team to ensure the final product exceeds expectations.

Please note: For general text, we use Avenir. The brand guidelines are slightly out of date and don't have correct imaging. Colours are correct though.

```html
<!DOCTYPE html>
<html lang="en">
<head>
<meta charset="utf-8">
<title>Velmora Business Cards</title>
<link href="https://fonts.googleapis.com/css2?family=Nunito+Sans:wght@400;600;700&display=swap" rel="stylesheet">
<style>
  :root {
    --page-bg: #ece8e4;
    --plum: #5e3478;
    --magenta: #b4307f;
    --accent-pink: #e6237e;
    --mark-pink: #d04a94;
    --white: #ffffff;
    --ink: #4d4d4d;
    --icon-plum: #6a3a82;
    --shadow: rgba(40, 20, 10, 0.35);
  }
  * { box-sizing: border-box; margin: 0; padding: 0; }
  html, body {
    width: 900px; height: 1200px; overflow: hidden;
    background: var(--page-bg);
    font-family: "Nunito Sans", "Avenir", sans-serif;
  }
  .card {
    position: absolute; left: 88px; width: 734px; height: 429px;
    border-radius: 24px; overflow: hidden;
    box-shadow: 0 4px 10px var(--shadow);
    background: linear-gradient(100deg, var(--plum) 0%, #8a337d 55%, var(--magenta) 100%);
  }
  .card--front { top: 137px; }
  .card--back { top: 632px; }
  .front-wave { position: absolute; inset: 0; width: 100%; height: 100%; }

  .brand { display: flex; align-items: center; }
  .brand__mark { flex: none; border-radius: 50%; background: var(--mark-pink); }
  .brand__name { color: var(--white); font-weight: 600; line-height: 1; }
  .tagline { color: var(--white); font-weight: 400; }

  .front-brand { position: absolute; left: 52px; top: 96px; }
  .front-brand .brand__mark { width: 50px; height: 50px; }
  .front-brand .brand__name { font-size: 46px; margin-left: 14px; }
  .front-brand .tagline { font-size: 14px; margin: 16px 0 0 84px; }

  .holder { position: absolute; right: 35px; top: 42px; text-align: right; color: var(--white); }
  .holder__name { font-size: 25px; font-weight: 400; letter-spacing: 0.5px; }
  .holder__name strong { font-weight: 700; }
  .holder__title { font-size: 17px; margin-top: 4px; letter-spacing: 0.5px; }

  .contacts { position: absolute; right: 37px; top: 279px; list-style: none; }
  .contacts li {
    display: flex; justify-content: flex-end; align-items: center; gap: 9px;
    height: 35.5px; font-size: 19px; color: var(--ink); letter-spacing: 1px;
  }
  .contacts svg { width: 20px; height: 20px; flex: none; }

  .back-brand { position: absolute; left: 205px; top: 150px; }
  .back-brand .brand__mark { width: 60px; height: 60px; }
  .back-brand .brand__name { font-size: 58px; margin-left: 42px; }
  .back-brand .tagline { font-size: 16px; margin: 14px 0 0 128px; }

  .back-web {
    position: absolute; left: 0; right: 0; top: 380px; text-align: center;
    color: var(--white); font-size: 16px; letter-spacing: 0.5px;
  }
  .back-web span { color: var(--accent-pink); }
</style>
</head>
<body>

<section class="card card--front">
  <svg class="front-wave" viewBox="0 0 734 429" preserveAspectRatio="none" aria-hidden="true">
    <defs>
      <linearGradient id="lipGrad" x1="0" x2="1" y1="0" y2="0">
        <stop offset="0" stop-color="#c2307f"/>
        <stop offset="0.7" stop-color="#a93080"/>
        <stop offset="1" stop-color="#5e3478"/>
      </linearGradient>
    </defs>
    <path d="M0,252 C60,358 150,392 222,384 C332,374 420,148 580,122 C652,112 712,182 734,246 L734,429 L0,429 Z" fill="url(#lipGrad)"/>
    <path d="M0,263 C60,364 150,402 222,394 C332,386 420,160 582,132 C652,122 712,192 734,258 L734,429 L0,429 Z" fill="#ffffff"/>
  </svg>

  <div class="front-brand">
    <div class="brand">
      <span class="brand__mark"></span>
      <span class="brand__name">Velmora</span>
    </div>
    <p class="tagline">people first, always</p>
  </div>

  <div class="holder">
    <p class="holder__name"><strong>DANIEL</strong> ASHFORD</p>
    <p class="holder__title">Founder and CEO</p>
  </div>

  <ul class="contacts">
    <li>+ 4 (000) 000 5555
      <svg viewBox="0 0 20 20" aria-hidden="true"><circle cx="10" cy="10" r="10" fill="#4caf50"/><path d="M7 5.5c.5-.3 1-.2 1.3.3l.9 1.6c.2.4.1.8-.2 1.1l-.6.5c.5 1.1 1.3 1.9 2.4 2.4l.5-.6c.3-.3.7-.4 1.1-.2l1.6.9c.5.3.6.8.3 1.3-.6 1-1.6 1.5-2.7 1.1C9.1 13.2 6.8 10.9 6 8.4c-.4-1.1.1-2.3 1-2.9z" fill="#fff"/></svg>
    </li>
    <li>ashford@velmora.com
      <svg viewBox="0 0 20 20" aria-hidden="true"><rect x="1" y="4" width="18" height="13" rx="2" fill="var(--icon-plum)"/><path d="M2 5.5l8 6 8-6" fill="none" stroke="#fff" stroke-width="1.6"/></svg>
    </li>
    <li>www.velmora.com
      <svg viewBox="0 0 20 20" aria-hidden="true"><g fill="none" stroke="var(--accent-pink)" stroke-width="1.5"><circle cx="10" cy="10" r="8.5"/><ellipse cx="10" cy="10" rx="3.8" ry="8.5"/><path d="M1.5 10h17M3 5.5h14M3 14.5h14"/></g></svg>
    </li>
  </ul>
</section>

<section class="card card--back">
  <div class="back-brand">
    <div class="brand">
      <span class="brand__mark"></span>
      <span class="brand__name">Velmora</span>
    </div>
    <p class="tagline">people first, always</p>
  </div>
  <p class="back-web">www.<span>velmora</span>.com</p>
</section>

</body>
</html>
```